Letterhead - Pelvarosi Law Group

I receive a fantastic logo from you guys and I'd like to incorporate it into business cards and letterhead. I accidentally approved design No. 58027913 and contacted designer Tarveck, and Tarveck sent me the zip folder for Design No. 58027986, which I very much appreciate.
I'd like to order business cards and letterhead with Design No. 58027986 as soon as possible, but I want to make sure that you incorporate the correct design (attached). I'd also like to provide my information to add (address, phone number, email, fax) but I'm not quite sure how to do it.
The information that I would like on the business cards and letterhead is as follows:
Pelvarosi Law Group
Dorian K. Pelvarosi, Esq.
2741 Halvern Street, Suite 306
Marrowgate, CA 94382
Office: (415) 738-0461
Fax: (415) 386-7710
dory@pelvarosilawgroup.com
Thanks in advance for any guidance.
Dory Pelvarosi
Pelvarosi Law Group
(415) 574-8839 (cell)

```html
<!DOCTYPE html>
<html lang="en">
<head>
<meta charset="utf-8">
<title>Pelvarosi Law Group – Letterhead</title>
<link rel="stylesheet" href="https://fonts.googleapis.com/css2?family=Arimo:wght@400;700&display=swap">
<style>
  :root {
    --brand-blue: #1b8fd0;
    --ink: #2a2a2a;
    --ink-soft: #3a3a3a;
    --backdrop: #e9e9ea;
    --paper: #ffffff;
  }
  * { box-sizing: border-box; margin: 0; padding: 0; }
  html, body {
    width: 1200px; height: 874px; overflow: hidden;
    background: var(--backdrop);
    font-family: "Arimo", Arial, sans-serif;
    color: var(--ink);
  }
  .letterhead {
    position: absolute; left: 300px; top: 13px;
    width: 600px; height: 848px;
    background: var(--paper);
    overflow: hidden;
    box-shadow: 0 2px 10px rgba(0,0,0,.08);
  }
  .corner { position: absolute; display: block; }
  .corner--top { top: 0; right: 0; }
  .corner--bottom { bottom: 0; left: 0; }

  .header {
    position: absolute; left: 40px; right: 40px; top: 78px;
    height: 84px;
    display: flex; align-items: flex-end; justify-content: space-between;
  }
  .firm-mark {
    font-size: 21px; font-weight: 700; color: var(--ink);
    letter-spacing: .3px; padding-bottom: 6px;
  }
  .header-info { display: flex; align-items: stretch; gap: 10px; font-size: 9.5px; line-height: 1.35; }
  .sender { text-align: right; color: var(--ink-soft); font-style: normal; }
  .sender__firm { color: var(--brand-blue); font-weight: 700; }
  .divider { width: 1px; background: var(--brand-blue); }
  .contacts { list-style: none; color: var(--ink-soft); }
  .contacts li { display: flex; align-items: center; gap: 5px; }
  .contacts svg { width: 9px; height: 9px; fill: var(--brand-blue); flex: none; }
  .header-rule {
    position: absolute; left: 40px; right: 40px; top: 170px;
    height: 2.5px; background: var(--brand-blue);
  }

  .letter {
    position: absolute; left: 72px; right: 44px; top: 232px;
    font-size: 10.3px; line-height: 1.5; color: var(--ink-soft);
  }
  .letter p { margin-bottom: 14px; }
  .letter .salutation { margin-bottom: 12px; }
  .closing { margin-top: 4px; }
  .signature {
    display: block; width: 150px; height: 30px; margin: 6px 0 4px 18px;
    background: linear-gradient(90deg, rgba(27,143,208,.35), rgba(27,143,208,.15));
    border-radius: 4px;
  }
  .signoff { margin-left: 40px; line-height: 1.5; }
</style>
</head>
<body>
  <main class="letterhead">
    <svg class="corner corner--top" width="200" height="130" viewBox="0 0 200 130" aria-hidden="true">
      <path d="M40 0 H200 V130 Q175 15 40 0 Z" fill="var(--brand-blue)"/>
    </svg>
    <svg class="corner corner--bottom" width="230" height="130" viewBox="0 0 230 130" aria-hidden="true">
      <path d="M0 0 V130 H230 Q25 115 0 0 Z" fill="var(--brand-blue)"/>
    </svg>

    <header class="header">
      <div class="firm-mark">Pelvarosi Law Group</div>
      <div class="header-info">
        <address class="sender">
          <div class="sender__firm">Pelvarosi Law Group</div>
          <div>Dorian K. Pelvarosi, Esq.</div>
          <div>2741 Halvern Street, Suite 306</div>
          <div>Marrowgate, CA 94382</div>
        </address>
        <span class="divider"></span>
        <ul class="contacts">
          <li><svg viewBox="0 0 10 10"><path d="M2 1 L4 1 L4.6 3 L3.4 3.8 Q4.2 5.8 6.2 6.6 L7 5.4 L9 6 L9 8 Q5 9 2 6 Q0.8 3.5 2 1Z"/></svg>(415) 738-0461</li>
          <li><svg viewBox="0 0 10 10"><rect x="3" y="0.5" width="4" height="3"/><rect x="1" y="3.5" width="8" height="4" rx="1"/><rect x="3" y="6.5" width="4" height="3"/></svg>(415) 386-7710</li>
          <li><svg viewBox="0 0 10 10"><path d="M0.5 2 H9.5 V8 H0.5Z M0.5 2 L5 5.5 L9.5 2" stroke="#fff" stroke-width=".6"/></svg>dory@pelvarosilawgroup.com</li>
          <li><svg viewBox="0 0 10 10"><circle cx="5" cy="5" r="4.5"/><path d="M0.5 5 H9.5 M5 0.5 Q2.5 5 5 9.5 M5 0.5 Q7.5 5 5 9.5" stroke="#fff" stroke-width=".6" fill="none"/></svg>www.pelvarosilawgroup.com</li>
        </ul>
      </div>
    </header>
    <div class="header-rule"></div>

    <article class="letter">
      <p class="salutation">Dear Sir,</p>
      <p>Lorem ipsum dolor sit amet, consectetur adipiscing elit, sed do eiusmod tempor incididunt ut labore et dolore magna aliqua. Ut enim ad minim veniam, quis nostrud exercitation ullamco laboris nisi ut aliquip ex ea commodo consequat. Duis aute irure dolor in reprehenderit in voluptate velit esse cillum dolore eu fugiat nulla pariatur. Excepteur sint occaecat cupidatat non proident, sunt in culpa qui officia deserunt mollit anim id est laborum. It is a long established fact that a reader will be distracted by the readable content of a page when looking at its layout. The point of using Lorem Ipsum is that it has a more-or-less normal distribution of letters, as opposed to using ‘Content here, content here’, making it look like readable English.</p>
      <p>But I must explain to you how all this mistaken idea of denouncing pleasure and praising pain was born and I will give you a complete account of the system, and expound the actual teachings of the great explorer of the truth, the master-builder of human happiness. No one rejects, dislikes, or avoids pleasure itself, because it is pleasure, but because those who do not know how to pursue pleasure rationally encounter consequences that are extremely painful. Nor again is there anyone who loves or pursues or desires to obtain pain of itself, because it is pain, but because occasionally circumstances occur in which toil and pain can procure him some great pleasure.</p>
      <p>There are many variations of passages of Lorem Ipsum available, but the majority have suffered alteration in some form, by injected humour, or randomised words which don't look even slightly believable. If you are going to use a passage of Lorem Ipsum, you need to be sure there isn't anything embarrassing hidden in the middle of text. All the Lorem Ipsum generators on the Internet tend to repeat predefined chunks as necessary, making this the first true generator on the Internet.</p>
      <div class="closing">Best Regards</div>
      <span class="signature" role="img" aria-label="Handwritten signature in blue ink"></span>
      <div class="signoff">
        <div>Dory Pelvarosi</div>
        <div>Pelvarosi Law Group</div>
        <div>(415) 574-8839 (cell)</div>
      </div>
    </article>
  </main>
</body>
</html>
```